Pebblewick - a new nut butter brand in Switzerland

We are launching a new and innovative line of organic Nut Butters in Switzerland called Pebblewick. 340g round glass jar and require a cool label design for the front, back and top of the jar. Pebblewick soldier and our slogan is "Kernels from every far corner - stirred in Zurich". It must therefore include the "flavor". The back label wants to include product description and nutritional information. The top should include the brand name, flavor and maybe another image. Overall we want to convey a young and fun designs appealing to the local hipster movement. The label designs we like are Fennimore's Spread, Ottilie's and Mango Ritual.

Target Market(s)

Swiss hipster commutity

Industry/Entity Type

Food Production

Font styles to use
Sans Serif

Colors
85cae6
86cfc6
cadf82
fbf289
fee18a
f8ba93
f9ba93
f59296
eea4c8

Requirements
Must have
• "Almond butter" on the front. A graphic representation of a nut cracker that will serve as our logo - clean and fun (refer to mango ritual) in large font "Kernels from every far corner - stirred in Zurich" on the front; slightly smaller than the "Almond Butter"
Nice to have

```html
<!DOCTYPE html>
<html lang="en">
<head>
<meta charset="utf-8">
<title>Pebblewick Almond Butter – Front Label</title>
<link href="https://fonts.googleapis.com/css2?family=Ubuntu:wght@700&family=Noto+Serif:wght@600&display=swap" rel="stylesheet">
<style>
  :root{
    --stage:#e9e9e9;
    --label-bg:#eef1e3;
    --label-edge:#dfe4cc;
    --pattern-leaf:#e1ebc3;
    --title-brown:#4a230f;
    --title-cream:#f1d3a8;
    --mascot-disc:#f1c68f;
    --mascot-disc-light:#f5d8b0;
    --pill-green:#8dc63f;
    --pill-text:#ffffff;
    --weight-text:#5a3a24;
  }
  html,body{margin:0;padding:0;overflow:hidden;}
  body{
    width:1200px;height:938px;background:var(--stage);
    position:relative;font-family:"Ubuntu",sans-serif;
  }
  .front-label{
    position:absolute;left:220px;top:69px;width:760px;height:800px;
    background:var(--label-bg);border:1px solid var(--label-edge);
    box-sizing:border-box;overflow:hidden;
  }
  .label-pattern{
    position:absolute;inset:0;
    background:
      radial-gradient(circle at 22% 35%, var(--pattern-leaf) 0, transparent 38%),
      radial-gradient(circle at 78% 62%, var(--pattern-leaf) 0, transparent 36%),
      radial-gradient(circle at 40% 85%, var(--pattern-leaf) 0, transparent 30%);
  }
  .product-title{
    position:absolute;left:50%;top:148px;transform:translateX(-50%);
    width:336px;margin:0;text-align:center;font-weight:700;
  }
  .product-title .line-one{
    display:block;font-size:80px;line-height:.95;color:var(--title-brown);letter-spacing:1px;
  }
  .product-title .line-two{
    display:block;margin-top:4px;background:var(--title-brown);color:var(--title-cream);
    font-size:70px;line-height:68px;height:68px;letter-spacing:5px;
  }
  .mascot-disc{
    position:absolute;left:50%;top:372px;transform:translateX(-50%);
    width:270px;height:270px;border-radius:50%;
    background:radial-gradient(circle at 50% 45%, var(--mascot-disc-light), var(--mascot-disc));
  }
  .slogan-pill{
    position:absolute;left:50%;top:640px;transform:translateX(-50%);
    width:340px;margin:0;padding:8px 14px;box-sizing:border-box;
    background:var(--pill-green);border-radius:16px;
    font-family:"Noto Serif",serif;font-weight:600;font-size:21px;line-height:1.25;
    color:var(--pill-text);text-align:center;letter-spacing:.5px;
  }
  .net-weight{
    position:absolute;left:0;right:0;top:728px;margin:0;text-align:center;
    font-family:"Noto Serif",serif;font-weight:600;font-size:21px;color:var(--weight-text);
  }
</style>
</head>
<body>
  <section class="front-label">
    <div class="label-pattern" role="img" aria-label="Soft pale green leaf texture with scattered almond icons"></div>
    <h1 class="product-title">
      <span class="line-one">Almond</span>
      <span class="line-two">Butter</span>
    </h1>
    <div class="mascot-disc" role="img" aria-label="Pebblewick soldier mascot holding a halberd, standing in an orange circle"></div>
    <p class="slogan-pill">Kernels from every far corner - stirred in Zurich</p>
    <p class="net-weight">340g</p>
  </section>
</body>
</html>
```